Business Card Design

we are a brand new cable TV network devoted to self improvement and leading a better life called FLOURISH TV.I have a logo. We have 3 executives that need cards.I want it to be a heavy stock card: professional but showing our creative nature

Industry/Entity Type

Business

Contact Information for Business Card

CLAUDIA SAENZ AMLIECEO350 San Juan DrPonte Vedra Beach FL 32082904-473-5953

```html
<!DOCTYPE html>
<html lang="en">
<head>
<meta charset="utf-8">
<title>Flourish TV — Business Card</title>
<link rel="stylesheet" href="https://fonts.googleapis.com/css2?family=Open+Sans:wght@400;600&display=swap">
<style>
  :root {
    --backdrop: #8d8e90;
    --card-paper: #ebebed;
    --brand-red: #a81c24;
    --red-dark: #7e1a1f;
    --red-bright: #c41e26;
    --ink: #2a2a2a;
    --ink-soft: #3a3a3a;
    --divider: #9a9a9a;
    --white: #ffffff;
  }
  * { margin: 0; padding: 0; box-sizing: border-box; }
  html, body {
    width: 1105px;
    height: 1200px;
    overflow: hidden;
    background: var(--backdrop);
    font-family: "Open Sans", Arial, sans-serif;
  }
  .canvas { position: relative; width: 1105px; height: 1200px; }
  .card {
    position: absolute;
    left: 182px;
    width: 748px;
    height: 427px;
  }
  .card-front { top: 119px; background: var(--card-paper); }
  .card-back  { top: 637px; }

  .wordmark {
    position: absolute;
    left: 262px;
    top: 318px;
    font-size: 38px;
    font-weight: 600;
    letter-spacing: -0.5px;
    color: var(--ink);
    line-height: 1;
  }
  .card-front .wordmark { left: 80px; top: 199px; }

  .divider {
    position: absolute;
    left: 388px;
    top: 141px;
    width: 1px;
    height: 154px;
    background: var(--divider);
  }
  .contact {
    position: absolute;
    left: 411px;
    top: 143px;
    color: var(--ink-soft);
    font-size: 18px;
    line-height: 25px;
  }
  .contact-name {
    color: var(--brand-red);
    font-weight: 600;
    font-size: 21px;
    letter-spacing: 0.3px;
    line-height: 30px;
  }
  .contact-role { margin-bottom: 14px; }
  .contact-phone { display: flex; align-items: center; gap: 8px; margin-top: 4px; }
  .contact-phone svg { width: 16px; height: 16px; fill: var(--brand-red); }

  .back-field {
    position: absolute;
    inset: 0;
    background: linear-gradient(90deg, var(--red-dark) 0%, var(--brand-red) 55%, var(--red-bright) 100%);
  }
  .card-back .wordmark {
    left: 0; right: 0; top: 190px;
    text-align: center;
    color: var(--white);
    font-size: 40px;
  }
</style>
</head>
<body>
<main class="canvas">
  <section class="card card-front">
    <div class="wordmark">FLOURISH TV</div>
    <div class="divider"></div>
    <div class="contact">
      <p class="contact-name">MARISOL DUVAL KERNO</p>
      <p class="contact-role">CEO</p>
      <p>718 Copper Hollow Ln</p>
      <p>Harbor Glen FL 30915</p>
      <p class="contact-phone">
        <svg viewBox="0 0 24 24" aria-hidden="true"><path d="M6.6 10.8a15.1 15.1 0 0 0 6.6 6.6l2.2-2.2a1 1 0 0 1 1-.25 11.4 11.4 0 0 0 3.6.57 1 1 0 0 1 1 1V20a1 1 0 0 1-1 1A17 17 0 0 1 3 4a1 1 0 0 1 1-1h3.5a1 1 0 0 1 1 1c0 1.25.2 2.45.57 3.57a1 1 0 0 1-.25 1z"/></svg>
        555-218-0476
      </p>
    </div>
  </section>

  <section class="card card-back">
    <div class="back-field" role="img" aria-label="Red gradient background with a repeating pattern of the brand symbol"></div>
    <div class="wordmark">FLOURISH TV</div>
  </section>
</main>
</body>
</html>
```